Natural Australian skin care company packaging for new product Bath salts

We are moving to fully refillable packaging and need someone to design our refill pouches. we have a number of products we need to do this for but our first one is our natural bath salts. This comes in a 200g tin in a pouch then the pouch can be bought to refill the tin. We can either print on the pouch or do sickers. The tin is a simple matt black tin with white text on the lid. the pouch comes in a gold colour. pictures are in the drop box lid.
Luxury bath salts Pouch - the dimensions are 60*55*180mm, , we can either print directly or do a sticker, We also need the sleeve to go around the tin. The dimensions of the tin are 65x65x70mm. The same text needs to go onto the sleeve as the pouch. The tin is black with white printing on the top (see picture).
Text is as follows
VT logo Quiet moss tide 100% pure magnesium bath salts
A rich fragrance of Australian wild flowers (using natural essential oils) with frangipani and gardenia. Sink into the natural ancient salt lake sourced 100% pure magnesium to replenish your skin. Transdermal absorption of magnesium is effective and contributes to electrolyte balance, normal muscle function and aids calcium absorption. The ultimate mineral reset.
Directions: Fill bath, once full put two heaped tablespoons of the salts into the bath (approx 50g). Climb in and relax.
Vell Tonic full logo
Country of Origin: Australia
PO Box 318
Kelbrin Shore 4862
QLD Australia
www.velltonic.com
ingredients:
magnesium chloride *, parfum **
*naturally sourced from ancient salt lakes
**a combination of essential oils and natural isolates.
e: 200g / 7.05 Oz
We also need the recycle, plastic free, not tested on animal eco friendly symbols.
Please use this link to our press assets and tin and pouch photos.
https://www.filevaultra.com/sh/kq3p81wmxt02hd5/QXtrNbLm__kwLzPeYd-HsnqWjLa?dl=0

```html
<!DOCTYPE html>
<html lang="en">
<head>
<meta charset="utf-8">
<title>Vell Tonic – Magnesium Bath Salts Packaging</title>
<link rel="stylesheet" href="https://fonts.googleapis.com/css2?family=Zilla+Slab:wght@300;400;500;600;700&display=swap">
<style>
  :root {
    --page: #ffffff;
    --kraft: #c8a072;
    --kraft-ink: #2a241d;
    --tin: #141414;
    --tin-ink: #f2f2f2;
    --font-slab: "Zilla Slab", Georgia, serif;
  }
  * { box-sizing: border-box; margin: 0; padding: 0; }
  html, body { width: 909px; height: 1200px; overflow: hidden; }
  body {
    background: var(--page);
    font-family: var(--font-slab);
    display: grid;
    grid-template-columns: 410px 410px;
    grid-template-rows: 430px 500px;
    column-gap: 29px;
    row-gap: 70px;
    padding: 100px 30px;
  }

  .panel {
    position: relative;
    display: flex;
    flex-direction: column;
    align-items: center;
    text-align: center;
    color: var(--ink);
  }
  .panel--kraft {
    --ink: var(--kraft-ink);
    background: var(--kraft);
    border-radius: 8px;
    padding: 26px 28px 20px;
  }
  .panel--kraft::before {
    content: "";
    position: absolute;
    inset: 8px;
    border: 1px dotted var(--kraft-ink);
    border-radius: 6px;
    pointer-events: none;
  }
  .panel--tin {
    --ink: var(--tin-ink);
    background: var(--tin);
    border-radius: 10px;
    padding: 44px 30px 28px;
  }

  /* brand lockup */
  .brand { display: flex; flex-direction: column; align-items: center; }
  .brand__dot {
    width: 26px; height: 26px; border-radius: 50%;
    border: 2px solid var(--ink);
    margin-bottom: 10px;
  }
  .brand__name {
    font-weight: 700;
    font-size: 22px;
    letter-spacing: 0.5px;
    text-transform: uppercase;
    line-height: 1;
  }
  .brand__tagline {
    font-weight: 700;
    font-size: 7px;
    letter-spacing: 0.6px;
    text-transform: uppercase;
    margin-top: 4px;
  }

  .divider-ornament {
    display: block;
    width: 58px; height: 2px;
    background: var(--ink);
    opacity: 0.75;
    margin: 9px auto 12px;
  }

  .title__kicker { font-weight: 300; font-size: 24px; line-height: 1.1; }
  .title__main {
    font-weight: 700;
    font-size: 40px;
    letter-spacing: 1px;
    line-height: 1;
    text-transform: uppercase;
  }
  .title--small .title__kicker { font-size: 15px; }
  .title--small .title__main { font-size: 24px; }

  .scent { font-size: 12px; line-height: 1.35; margin-top: 12px; max-width: 260px; }
  .rule { width: 60px; height: 1px; background: var(--ink); margin: 12px auto 10px; }
  .note { font-size: 11px; font-weight: 300; }
  .weight { font-size: 11px; margin-top: auto; letter-spacing: 0.3px; }

  .copy { font-size: 9.6px; line-height: 1.4; }
  .copy p + p { margin-top: 9px; }
  .copy strong { font-weight: 600; }
  .copy .gap { display: inline-block; width: 8px; }

  .back-footer {
    margin-top: auto;
    width: 100%;
    display: flex;
    justify-content: space-between;
    align-items: flex-end;
    text-align: left;
  }
  .back-footer .brand { align-items: flex-start; }
  .back-footer .brand__name { font-size: 12px; }
  .back-footer .brand__tagline { font-size: 4.5px; margin-top: 2px; }
  .contact { font-size: 8.4px; line-height: 1.35; margin-top: 6px; }
  .badges-block { display: flex; flex-direction: column; align-items: center; gap: 10px; }
  .badges { display: flex; gap: 7px; }
  .badge {
    width: 22px; height: 22px; border-radius: 50%;
    border: 1.6px solid var(--ink);
  }
  .badges-block .weight { margin-top: 0; font-size: 9px; }
</style>
</head>
<body>

  <!-- refill pouch label: back -->
  <section class="panel panel--kraft panel--back">
    <div class="title title--small">
      <p class="title__kicker">100% Pure Magnesium</p>
      <h2 class="title__main">Bath Salts</h2>
    </div>
    <span class="divider-ornament" role="img" aria-label="Small arrow divider ornament"></span>
    <div class="copy">
      <p>A rich fragrance of Australian wild flowers (using natural essential oils) with frangipani and gardenia. Sink into the natural ancient salt lake sourced 100% pure magnesium to replenish your skin. Transdermal absorption of magnesium is effective and contributes to electrolyte balance, normal muscle function and aids calcium absorption. The ultimate mineral reset.</p>
      <p><strong>Directions:</strong> Fill bath, once full put two heaped tablespoons of the salts into the bath (approx 50g). Climb in and relax.</p>
      <p><strong>Ingredients:</strong><span class="gap"></span><strong>Magnesium chloride *, Parfum **</strong><br>*Naturally sourced from ancient salt lakes<br>**A combination of essential oils and natural isolates.</p>
    </div>
    <footer class="back-footer">
      <div>
        <div class="brand">
          <span class="brand__name">Vell Tonic</span>
          <span class="brand__tagline">Australian Bush Medicines</span>
        </div>
        <p class="contact">Country of Origin: Australia<br>PO Box 318, Kelbrin Shore 4862<br>QLD Australia<br>www.velltonic.com</p>
      </div>
      <div class="badges-block">
        <div class="badges">
          <span class="badge" role="img" aria-label="Recyclable symbol"></span>
          <span class="badge" role="img" aria-label="Plastic free symbol"></span>
          <span class="badge" role="img" aria-label="Not tested on animals symbol"></span>
          <span class="badge" role="img" aria-label="Eco friendly symbol"></span>
        </div>
        <p class="weight">200G / 7.05 OZ ℮</p>
      </div>
    </footer>
  </section>

  <!-- refill pouch label: front -->
  <section class="panel panel--kraft panel--front">
    <div class="brand">
      <span class="brand__dot"></span>
      <span class="brand__name">Vell Tonic</span>
      <span class="brand__tagline">Australian Bush Medicines</span>
    </div>
    <span class="divider-ornament" role="img" aria-label="Small arrow divider ornament"></span>
    <div class="title">
      <p class="title__kicker">100% Pure Magnesium</p>
      <h1 class="title__main">Bath Salts</h1>
    </div>
    <p class="scent">A rich fragrance of Australian wild flowers with frangipani and gardenia.</p>
    <span class="rule"></span>
    <p class="note">Using natural essential oils</p>
    <p class="weight">200G / 7.05 OZ ℮</p>
  </section>

  <!-- tin sleeve: front -->
  <section class="panel panel--tin panel--front">
    <div class="brand">
      <span class="brand__dot"></span>
      <span class="brand__name">Vell Tonic</span>
      <span class="brand__tagline">Australian Bush Medicines</span>
    </div>
    <span class="divider-ornament" role="img" aria-label="Small arrow divider ornament"></span>
    <div class="title">
      <p class="title__kicker">100% Pure Magnesium</p>
      <h1 class="title__main">Bath Salts</h1>
    </div>
    <p class="scent">A rich fragrance of Australian wild flowers with frangipani and gardenia.</p>
    <span class="rule"></span>
    <p class="note">Using natural essential oils</p>
    <p class="weight">200G / 7.05 OZ ℮</p>
  </section>

  <!-- tin sleeve: back -->
  <section class="panel panel--tin panel--back">
    <div class="title title--small">
      <p class="title__kicker">100% Pure Magnesium</p>
      <h2 class="title__main">Bath Salts</h2>
    </div>
    <span class="divider-ornament" role="img" aria-label="Small arrow divider ornament"></span>
    <div class="copy">
      <p>A rich fragrance of Australian wild flowers (using natural essential oils) with frangipani and gardenia. Sink into the natural ancient salt lake sourced 100% pure magnesium to replenish your skin. Transdermal absorption of magnesium is effective and contributes to electrolyte balance, normal muscle function and aids calcium absorption. The ultimate mineral reset.</p>
      <p><strong>Directions:</strong> Fill bath, once full put two heaped tablespoons of the salts into the bath (approx 50g). Climb in and relax.</p>
      <p><strong>Ingredients:</strong><span class="gap"></span><strong>Magnesium chloride *, Parfum **</strong><br>*Naturally sourced from ancient salt lakes<br>**A combination of essential oils and natural isolates.</p>
    </div>
    <footer class="back-footer">
      <div>
        <div class="brand">
          <span class="brand__name">Vell Tonic</span>
          <span class="brand__tagline">Australian Bush Medicines</span>
        </div>
        <p class="contact">Country of Origin: Australia<br>PO Box 318, Kelbrin Shore 4862<br>QLD Australia<br>www.velltonic.com</p>
      </div>
      <div class="badges-block">
        <div class="badges">
          <span class="badge" role="img" aria-label="Recyclable symbol"></span>
          <span class="badge" role="img" aria-label="Plastic free symbol"></span>
          <span class="badge" role="img" aria-label="Not tested on animals symbol"></span>
          <span class="badge" role="img" aria-label="Eco friendly symbol"></span>
        </div>
        <p class="weight">200G / 7.05 OZ ℮</p>
      </div>
    </footer>
  </section>

</body>
</html>
```